Business card for a new cabinet shop company named Marlowe Cabinets for high end cabinets

Design a business card, thinking dark rich green with colours to speak of high end luxury ie; cream, gold, black possibly

Peter Lindqvar
Director Craftsman
Email: info@marlowecabinets.com.au
Instagram : @marlowe.cabinets

```html
<!DOCTYPE html>
<html lang="en">
<head>
<meta charset="utf-8">
<title>Marlowe Cabinets — Business Card</title>
<link href="https://fonts.googleapis.com/css2?family=Jost:wght@400;500&display=swap" rel="stylesheet">
<style>
  :root {
    --backdrop: #1c1c1e;
    --green: #0a4229;
    --black: #1d1d1d;
    --gold: #c9ac67;
    --cream: #f4f1ea;
  }
  * { box-sizing: border-box; margin: 0; padding: 0; }
  html, body {
    width: 1200px; height: 801px; overflow: hidden;
    background: var(--backdrop);
    font-family: "Jost", "Futura", sans-serif;
  }
  .stage {
    width: 1200px; height: 801px;
    display: flex; align-items: center; justify-content: center; gap: 48px;
  }
  .card {
    width: 530px; height: 324px;
    border: 2px solid var(--gold);
    position: relative; overflow: hidden;
  }

  /* Front */
  .card--front {
    background: var(--green);
    display: flex; align-items: center; justify-content: center;
  }
  .brand {
    display: flex; align-items: center; gap: 16px;
    color: var(--gold); font-weight: 500; letter-spacing: 0.02em;
  }
  .brand__mark {
    width: 14px; height: 14px; border: 2px solid var(--gold);
  }
  .card--front .brand { font-size: 40px; }

  /* Back */
  .card--back { background: var(--black); }
  .back__top {
    height: 57%; background: var(--green);
    border-bottom: 2px solid var(--gold);
    display: flex; align-items: center; justify-content: center;
    padding-left: 20px;
  }
  .card--back .brand { font-size: 34px; }
  .back__bottom {
    height: 43%;
    display: flex; align-items: center; justify-content: center;
    gap: 22px; padding: 0 24px;
  }
  .person { text-align: right; }
  .person__name {
    color: var(--gold); font-size: 25px; font-weight: 500; line-height: 1.1;
  }
  .person__role {
    color: var(--cream); font-size: 13px; letter-spacing: 0.08em; margin-top: 2px;
  }
  .divider { width: 1px; height: 72px; background: var(--gold); }
  .contacts { list-style: none; display: flex; flex-direction: column; gap: 7px; }
  .contacts li {
    display: flex; align-items: center; gap: 9px;
    color: var(--cream); font-size: 13px; letter-spacing: 0.02em;
  }
  .contacts svg { width: 12px; height: 12px; flex: none; }
  .dot { width: 10px; height: 10px; border: 1.5px solid var(--gold); border-radius: 50%; flex: none; margin: 0 1px; }
</style>
</head>
<body>
  <main class="stage">
    <section class="card card--front" aria-label="Card front">
      <div class="brand"><span class="brand__mark"></span><span>Marlowe Cabinets</span></div>
    </section>

    <section class="card card--back" aria-label="Card back">
      <div class="back__top">
        <div class="brand"><span class="brand__mark"></span><span>Marlowe Cabinets</span></div>
      </div>
      <div class="back__bottom">
        <div class="person">
          <p class="person__name">Peter Lindqvar</p>
          <p class="person__role">Director Craftsman</p>
        </div>
        <span class="divider"></span>
        <ul class="contacts">
          <li><span class="dot"></span>@marlowe.cabinets</li>
          <li>
            <svg viewBox="0 0 12 12" aria-hidden="true"><rect x="0.5" y="2" width="11" height="8" fill="none" stroke="#c9ac67"/><path d="M0.5 2 L6 6.5 L11.5 2" fill="none" stroke="#c9ac67"/></svg>
            info@marlowecabinets.com.au
          </li>
          <li>
            <svg viewBox="0 0 12 12" aria-hidden="true"><circle cx="6" cy="6" r="5.3" fill="none" stroke="#c9ac67"/><ellipse cx="6" cy="6" rx="2.3" ry="5.3" fill="none" stroke="#c9ac67"/><path d="M0.7 6 H11.3" stroke="#c9ac67"/></svg>
            marlowecabinets.com.au
          </li>
        </ul>
      </div>
    </section>
  </main>
</body>
</html>
```